We have a new logo so we need to change our business card

We're super Happy with our current cards but I think with a new logo should come a new design. I wouldn't mind seeing the icons that we used on the back last time reused on this card. Please feel free to visit our website to get a sense for our brand www.brindlewick.ca

I need the final final to have contact info for:

Gordon Hasley
Co-Owner
info@brindlewick.ca
778-315-6207

and

Marjorie Hasley
Co-Owner
info@brindlewick.ca
778-342-5810

Target Market(s)

Female dog owners, 21 to 70

Industry/Entity Type

pet industry

Contact Information for Business Card

included in brief

Requirements
Should not have
• We do not want it to look cartonish

```html
<!DOCTYPE html>
<html lang="en">
<head>
<meta charset="utf-8">
<title>Brindlewick Business Card</title>
<link href="https://fonts.googleapis.com/css2?family=Quicksand:wght@500;600;700&display=swap" rel="stylesheet">
<style>
  :root {
    --green: #8fce5a;
    --green-dark: #7cc043;
    --ink: #2b2b2b;
    --black: #111111;
    --white: #ffffff;
    --paper: #b8b8b8;
    --faint: #f0f1ee;
    --faint-dark: #1d1d1d;
  }
  * { box-sizing: border-box; margin: 0; padding: 0; }
  html, body { width: 1200px; height: 876px; overflow: hidden; }
  body {
    background: var(--paper);
    font-family: "Quicksand", sans-serif;
    display: flex;
    flex-direction: column;
    align-items: center;
    justify-content: center;
    gap: 56px;
  }
  .card {
    position: relative;
    width: 630px;
    height: 360px;
    overflow: hidden;
    box-shadow: 0 10px 24px rgba(0,0,0,.25);
  }

  /* Front */
  .card-front { background: var(--white); }
  .front-band {
    position: absolute; left: 0; top: 0; bottom: 0; width: 78px;
    background: var(--green);
    border-right: 10px solid var(--ink);
  }
  .front-mark {
    position: absolute; left: 36px; top: 40px;
    width: 150px; height: 150px; border-radius: 50%;
    background: var(--green);
    box-shadow: 0 0 0 12px var(--white);
  }
  .front-faint {
    position: absolute; right: -90px; bottom: -120px;
    width: 230px; height: 230px; border-radius: 50%;
    background: var(--faint);
  }
  .front-content { position: absolute; left: 216px; top: 96px; right: 20px; }
  .wordmark {
    font-family: "Quicksand", sans-serif;
    font-weight: 700;
    line-height: 1;
  }
  .front-content .wordmark { font-size: 60px; color: var(--ink); }
  .person { margin-top: 34px; }
  .person-name { font-size: 30px; font-weight: 700; color: var(--ink); line-height: 1.05; }
  .person-name .first { color: var(--green-dark); }
  .person-role { font-size: 15px; font-weight: 600; color: var(--ink); margin-top: 4px; }
  .contact {
    display: flex; align-items: center; gap: 10px;
    font-size: 15px; font-weight: 600; color: var(--ink); margin-top: 8px;
  }
  .contact-item { display: flex; align-items: center; gap: 6px; }
  .contact-divider { width: 1px; height: 18px; background: var(--ink); }
  .contact svg { width: 16px; height: 16px; }

  /* Back */
  .card-back { background: var(--black); }
  .back-faint {
    position: absolute; right: 40px; top: 150px;
    width: 200px; height: 200px; border-radius: 50%;
    background: var(--faint-dark);
  }
  .back-logo {
    position: absolute; left: 70px; top: 78px;
    display: flex; align-items: center; gap: 16px;
  }
  .back-mark { width: 64px; height: 64px; border-radius: 50%; background: var(--green); flex: none; }
  .back-logo .wordmark { font-size: 54px; color: var(--white); }
  .back-band {
    position: absolute; left: 0; right: 0; bottom: 0; height: 54px;
    background: var(--green);
    display: flex; align-items: center; padding-left: 70px;
  }
  .website {
    font-family: "Quicksand", sans-serif; font-weight: 700;
    font-size: 15px; letter-spacing: 6px; color: var(--ink);
  }
</style>
</head>
<body>
  <section class="card card-front">
    <div class="front-band"></div>
    <div class="front-faint"></div>
    <div class="front-mark"></div>
    <div class="front-content">
      <div class="wordmark">Brindlewick</div>
      <div class="person">
        <div class="person-name"><span class="first">Gordon</span> Hasley</div>
        <div class="person-role">Co-Owner</div>
        <div class="contact">
          <span class="contact-item">
            <svg viewBox="0 0 16 16" aria-hidden="true"><circle cx="8" cy="8" r="7" fill="none" stroke="#7cc043" stroke-width="1.5"/><path d="M5.5 4.5l1.5 1.5-1 1c.6 1.2 1.5 2.1 2.7 2.7l1-1 1.5 1.5-1 1.2C7.5 11 5 8.5 4.6 5.5z" fill="#7cc043"/></svg>
            778-315-6207
          </span>
          <span class="contact-divider"></span>
          <span class="contact-item">
            <svg viewBox="0 0 16 16" aria-hidden="true"><rect x="1" y="3" width="14" height="10" fill="#7cc043"/><path d="M1 3l7 6 7-6" fill="none" stroke="#fff" stroke-width="1.3"/></svg>
            info@brindlewick.ca
          </span>
        </div>
      </div>
    </div>
  </section>

  <section class="card card-back">
    <div class="back-faint"></div>
    <div class="back-logo">
      <div class="back-mark"></div>
      <div class="wordmark">Brindlewick</div>
    </div>
    <div class="back-band"><span class="website">www.brindlewick.ca</span></div>
  </section>
</body>
</html>
```